Gelato Business Card

create a new business card using existing logo

Target Market(s)

B2B

Contact Information for Business Card

typical contact info: logo, address, email, phone, rep name

Colors
0355a3
33a6d7

Requirements
Must have
• a feel of high quality, luxury, happiness
• use cool, comforting color and texture of business card.
Nice to have
• "A Little Perfection Goes A Long Way!" TM
• or, "more quality, more flavor"
• or, "Flavor Matters"

```html
<!DOCTYPE html>
<html lang="en">
<head>
<meta charset="utf-8">
<title>Marcello's Business Card</title>
<link href="https://fonts.googleapis.com/css2?family=Montserrat:wght@400;500;600&display=swap" rel="stylesheet">
<style>
  :root {
    --page: #e9e9eb;
    --card: #ffffff;
    --scoop-blue: #2f54a8;
    --accent-cyan: #33a6d7;
    --name-gold: #f2c230;
    --cone-yellow: #e2c020;
    --cone-orange: #e9845a;
    --text-grey: #6b6b6b;
    --brand-violet: #5b55c2;
  }
  * { margin: 0; padding: 0; box-sizing: border-box; }
  html, body {
    width: 1200px; height: 900px; overflow: hidden;
    background: var(--page);
    font-family: "Montserrat", sans-serif;
  }
  .card {
    position: absolute; left: 100px; top: 165px;
    width: 1000px; height: 571px;
    background: var(--card);
    overflow: hidden;
    box-shadow: 0 18px 40px rgba(0,0,0,0.18);
  }
  .artwork {
    position: absolute; left: 0; top: 0;
    width: 560px; height: 571px;
    background: linear-gradient(180deg,
      var(--scoop-blue) 0%, var(--scoop-blue) 52%,
      var(--cone-orange) 62%, var(--cone-yellow) 100%);
  }
  .rep {
    position: absolute; left: 250px; top: 170px;
    transform: rotate(-8deg);
  }
  .rep-name { color: var(--name-gold); font-size: 38px; font-weight: 600; line-height: 1.15; }
  .rep-title { color: #ffffff; font-size: 28px; font-weight: 400; margin-left: 12px; }
  .brand {
    position: absolute; right: 90px; top: 66px;
    display: flex; align-items: center; gap: 14px;
  }
  .brand-dot { width: 22px; height: 22px; border-radius: 50%; background: var(--brand-violet); }
  .brand-name { color: var(--brand-violet); font-size: 44px; font-weight: 600; }
  .address {
    position: absolute; right: 102px; top: 212px;
    text-align: right; color: var(--text-grey);
    font-size: 22px; line-height: 1.4; font-style: normal;
  }
  .contacts {
    position: absolute; right: 60px; top: 318px;
    list-style: none; color: var(--text-grey);
    font-size: 22px; line-height: 1.5;
  }
  .contacts li { display: flex; justify-content: flex-end; align-items: center; gap: 18px; }
  .contacts svg { width: 24px; height: 24px; flex: none; }
</style>
</head>
<body>
  <article class="card">
    <div class="artwork" role="img" aria-label="Illustration of a blue gelato scoop on a yellow-orange waffle cone"></div>

    <div class="rep">
      <div class="rep-name">John Doe</div>
      <div class="rep-title">Manager</div>
    </div>

    <div class="brand">
      <span class="brand-dot"></span>
      <span class="brand-name">Marcello's</span>
    </div>

    <address class="address">
      48 Harbour Lane<br>Lakeview, AB, T2K 4M8
    </address>

    <ul class="contacts">
      <li>403-555-0172
        <svg viewBox="0 0 24 24"><path fill="var(--accent-cyan)" d="M15,3 C10,4 8,8 8,12 C8,16 10,20 15,21 L16,18 C13,17 12,15 12,12 C12,9 13,7 16,6 Z"/></svg>
      </li>
      <li>john.doe@marcello's
        <svg viewBox="0 0 24 24"><rect x="2" y="5" width="20" height="14" fill="var(--accent-cyan)"/><path d="M2,5 L12,13 L22,5" fill="none" stroke="#fff" stroke-width="2"/></svg>
      </li>
      <li>www.marcello's.com
        <svg viewBox="0 0 24 24"><circle cx="12" cy="12" r="10" fill="var(--accent-cyan)"/><g fill="none" stroke="#fff" stroke-width="1.5"><ellipse cx="12" cy="12" rx="4" ry="10"/><path d="M2,12 H22 M4,7 H20 M4,17 H20"/></g></svg>
      </li>
    </ul>
  </article>
</body>
</html>
```